Salon website

Need a web design for a new blow dry and hair extension boutique in CT
would like the color scheme to be gray, white and tiffany blue
Create a web site with about 4 pages showing
1 about us page
1 blow dry services page
1 hair extension services page
1 contact us page
1 membership page
1 parties page

Industry/Entity Type

Boutique

Colors
86cfc6
cfeae6
33b7a4
aaaaaa
cbcbcb
ffffff

```html
<!DOCTYPE html>
<html lang="en">
<head>
<meta charset="utf-8">
<title>Lumen Blow Dry – Services</title>
<link href="https://fonts.googleapis.com/css2?family=Roboto:wght@300;400;500;700&display=swap" rel="stylesheet">
<style>
:root{
  --teal:#86cfc6;
  --teal-pale:#cfeae6;
  --teal-deep:#33b7a4;
  --charcoal:#5f5f5f;
  --ink:#333333;
  --text:#6f6f6f;
  --muted:#aaaaaa;
  --rule:#cbcbcb;
  --white:#ffffff;
  --footer-text:#cfcfcf;
  --footer-rule:#6d6d6d;
}
*{margin:0;padding:0;box-sizing:border-box}
html,body{width:900px;height:1200px;overflow:hidden;background:var(--white)}
body{position:relative;font-family:"Roboto",Arial,sans-serif;color:var(--text)}
.abs{position:absolute}

/* header */
.brand{left:45px;top:7px;width:140px;height:90px;background:var(--teal);box-shadow:0 0 6px rgba(0,0,0,.35);display:flex;align-items:center;justify-content:center;gap:7px}
.brand-dot{width:10px;height:10px;background:var(--charcoal)}
.brand-name{font-size:15px;font-weight:400;color:var(--charcoal);letter-spacing:1px;line-height:1.1}
.nav a{position:absolute;top:29px;font-size:12px;color:#555;text-decoration:none;text-transform:uppercase;font-weight:400}
.nav-active{left:478px;top:0;width:90px;height:75px;background:var(--charcoal)}
.nav-active::before{content:"";position:absolute;left:0;top:0;width:90px;height:4px;background:var(--teal)}
.nav-active::after{content:"";position:absolute;left:39px;top:4px;border:6px solid transparent;border-top-color:var(--teal)}
.nav a.current{color:var(--teal);left:499px;z-index:2}

/* info band */
.band{left:0;top:105px;width:900px;height:72px;background:var(--charcoal)}
.band-phone{left:45px;top:105px}
.phone-number{left:128px;top:120px;font-size:17px;color:var(--white);font-weight:400}
.city{left:134px;top:154px;font-size:10px;color:var(--white)}
.hours{right:45px;top:126px;font-size:11px;color:var(--white)}
.hours span{color:var(--teal)}

/* breadcrumb */
.crumb-rule{left:45px;width:810px;border-top:1px dashed #e2e2e2}
.crumb{top:226px;font-size:10px;text-transform:uppercase}
.crumb-sep{left:87px;top:225px;width:1px;height:14px;background:#e0e0e0}

/* service columns */
.svc{top:306px;width:170px}
.svc-kicker{font-size:11px;color:var(--ink);text-transform:uppercase;line-height:14px}
.svc-title{font-size:14px;color:var(--teal);text-transform:uppercase;line-height:20px;font-weight:400}
.svc-rule{margin-top:5px;border-top:1px dashed var(--rule);margin-bottom:8px}
.svc ul{list-style:none}
.svc li{font-size:9px;color:var(--text);height:24.5px;line-height:14px;display:flex;gap:4px;align-items:flex-start}
.svc li svg{margin-top:4px;flex:none}

/* highlights */
.section-title{font-size:19px;color:var(--ink);font-weight:400;text-transform:uppercase}
.lead{font-size:10px;font-weight:700;color:#777;line-height:18px}
.entry-head{font-size:12px;color:#555;text-transform:uppercase;line-height:16px}
.entry-head span{color:var(--teal)}
.entry-body{font-size:9.6px;line-height:17.5px;color:var(--text)}

/* treatments */
.treat{left:469px;width:380px;display:flex;gap:12px}
.treat-photo{width:48px;height:48px;border-radius:50%;flex:none}
.treat h4{font-size:10px;font-weight:700;color:#777;line-height:16px;margin-bottom:2px}
.treat p{font-size:9.6px;line-height:17.5px;color:var(--text)}

/* footer */
.footer{left:0;top:912px;width:900px;height:245px;background:var(--charcoal)}
.f-col{width:170px}
.f-title{font-size:13px;color:var(--teal);text-transform:uppercase;font-weight:400;padding-bottom:8px;border-bottom:1px solid var(--footer-rule)}
.f-text{font-size:9.6px;line-height:17.7px;color:var(--footer-text)}
.social{display:flex;gap:10px;margin-top:9px}
.social span{width:27px;height:27px;background:var(--white);display:block}
.f-link{color:var(--teal)}
.quote-mark{font-size:34px;font-weight:700;color:#3f3f3f;line-height:10px;vertical-align:-12px}
.cite{font-size:11px;color:#838383;text-align:right;margin-top:4px}
.copyright{left:45px;top:1173px;font-size:10px;color:#555}
</style>
</head>
<body>

<header>
  <div class="abs brand"><span class="brand-dot"></span><span class="brand-name">LUMEN<br>BLOW DRY</span></div>
  <nav class="nav">
    <div class="abs nav-active"></div>
    <a style="left:331px" href="#">Home</a>
    <a style="left:405px" href="#">About Us</a>
    <a class="current" href="#">Services</a>
    <a style="left:591px" href="#">Membership</a>
    <a style="left:704px" href="#">Parties</a>
    <a style="left:788px" href="#">Contact</a>
  </nav>
</header>

<section class="abs band"></section>
<svg class="abs band-phone" width="216" height="72" viewBox="0 0 216 72">
  <polygon points="0,0 216,0 174,72 0,72" fill="#86cfc6"/>
  <circle cx="63" cy="27" r="15" fill="none" stroke="#ffffff" stroke-opacity=".7" stroke-width="1"/>
  <path d="M56 21c1-2 3-2 4 0l1 2c1 1 0 2-1 3 1 2 2 4 4 5 1-1 2-2 3-1l2 1c2 1 2 3 0 4-3 2-7-1-10-4s-5-7-3-10z" fill="#ffffff"/>
</svg>
<div class="abs phone-number">1234567890</div>
<div class="abs city">City Name</div>
<div class="abs hours">TIMMINGS : <span>09.30 AM - 10.00PM</span></div>

<div class="abs crumb-rule" style="top:213px"></div>
<div class="abs crumb" style="left:45px;color:#555">Home</div>
<div class="abs crumb-sep"></div>
<div class="abs crumb" style="left:104px;color:var(--teal)">Services</div>
<div class="abs crumb-rule" style="top:251px"></div>

<svg width="0" height="0" style="position:absolute">
  <defs><symbol id="chev" viewBox="0 0 7 6"><path d="M0 0l3 3-3 3M3.5 0l3 3-3 3" fill="none" stroke="#555" stroke-width="1"/></symbol></defs>
</svg>

<section class="abs svc" style="left:57px">
  <div class="svc-kicker">Blow</div><div class="svc-title">Dry</div><div class="svc-rule"></div>
  <ul>
    <li><svg width="7" height="6"><use href="#chev"/></svg>Always free from repetition</li>
    <li><svg width="7" height="6"><use href="#chev"/></svg>Always free from repetition</li>
    <li><svg width="7" height="6"><use href="#chev"/></svg>The standard chunk of Lorem</li>
    <li><svg width="7" height="6"><use href="#chev"/></svg>The standard chunk of Lorem</li>
    <li><svg width="7" height="6"><use href="#chev"/></svg>Always free from repetition</li>
  </ul>
</section>
<section class="abs svc" style="left:263px">
  <div class="svc-kicker">Hair</div><div class="svc-title">Color</div><div class="svc-rule"></div>
  <ul>
    <li><svg width="7" height="6"><use href="#chev"/></svg>Always free from repetition</li>
    <li><svg width="7" height="6"><use href="#chev"/></svg>Always free from repetition</li>
    <li><svg width="7" height="6"><use href="#chev"/></svg>The standard chunk of Lorem</li>
    <li><svg width="7" height="6"><use href="#chev"/></svg>The standard chunk of Lorem</li>
    <li><svg width="7" height="6"><use href="#chev"/></svg>Always free from repetition</li>
  </ul>
</section>
<section class="abs svc" style="left:469px">
  <div class="svc-kicker">Hair</div><div class="svc-title">Spa</div><div class="svc-rule"></div>
  <ul>
    <li><svg width="7" height="6"><use href="#chev"/></svg>The standard chunk of Lorem</li>
    <li><svg width="7" height="6"><use href="#chev"/></svg>The standard chunk of Lorem</li>
    <li><svg width="7" height="6"><use href="#chev"/></svg>Always free from repetition</li>
    <li><svg width="7" height="6"><use href="#chev"/></svg>Always free from repetition</li>
    <li><svg width="7" height="6"><use href="#chev"/></svg>The standard chunk of Lorem</li>
  </ul>
</section>
<section class="abs svc" style="left:675px">
  <div class="svc-kicker">Hair</div><div class="svc-title">Extensions</div><div class="svc-rule"></div>
  <ul>
    <li><svg width="7" height="6"><use href="#chev"/></svg>Always free from repetition</li>
    <li><svg width="7" height="6"><use href="#chev"/></svg>Always free from repetition</li>
    <li><svg width="7" height="6"><use href="#chev"/></svg>The standard chunk of Lorem</li>
    <li><svg width="7" height="6"><use href="#chev"/></svg>The standard chunk of Lorem</li>
    <li><svg width="7" height="6"><use href="#chev"/></svg>Always free from repetition</li>
  </ul>
</section>

<section class="abs" style="left:57px;top:518px;width:360px">
  <h2 class="section-title">Highlights</h2>
  <p class="lead" style="margin-top:8px">Lorem ipsum dolor sit amet, consectetur adipisicing elit, sed do eiusmod tempor incididunt ut labore et dolore magna aliqua sed do eiusmod tempor.</p>
  <h3 class="entry-head" style="margin-top:8px;font-weight:400"><span>2013</span> - Sed do eiusmod tempor</h3>
  <p class="entry-body">Lorem ipsum dolor sit amet, consectetur adipisicing elit, sed do eiusmod tempor incididunt ut labore et dolore magna aliqua. Ut enim ad minim veniam, quis nostrud exercitation ullamco laboris nisi ut aliquip ex ea commodo consequat.</p>
  <h3 class="entry-head" style="margin-top:10px;font-weight:400"><span>2010</span> - Sed do eiusmod tempor</h3>
  <p class="entry-body">Lorem ipsum dolor sit amet, consectetur adipisicing elit, sed do eiusmod tempor incididunt ut labore et dolore magna aliqua. Ut enim ad minim veniam, quis nostrud exercitation ullamco laboris nisi ut aliquip ex ea commodo consequat.</p>
  <h3 class="entry-head" style="margin-top:10px;font-weight:400"><span>2008</span> - Sed do eiusmod tempor</h3>
  <p class="entry-body">Lorem ipsum dolor sit amet, consectetur adipisicing elit, sed do eiusmod tempor incididunt ut labore et dolore magna aliqua. Ut enim ad minim veniam, quis nostrud exercitation ullamco laboris nisi ut aliquip ex ea commodo consequat.</p>
</section>

<h2 class="abs section-title" style="left:469px;top:518px">Hair Treatments</h2>
<div class="abs treat" style="top:558px">
  <div class="treat-photo" role="img" aria-label="Photo of a stylist giving a client a blow dry" style="background:radial-gradient(circle at 40% 40%,#d9c3b0,#8a6a55)"></div>
  <div><h4>Hair Blow Dry</h4><p>sit amet, consectetuer adipiscing elit, sed diam nonummy nibh euismod tincidunt ut laoreet dolore magna aliquam erat volutpat. Ut wisi enim ad</p></div>
</div>
<div class="abs treat" style="top:628px">
  <div class="treat-photo" role="img" aria-label="Photo of long dark hair extensions" style="background:radial-gradient(circle at 50% 40%,#6a4a3a,#2a1b15)"></div>
  <div><h4>Hair Extensions</h4><p>dolor sit amet, consectetuer adipiscing elit, sed diam nonummy nibh euismod tincidunt ut laoreet dolore magna aliquam erat volutpat.</p></div>
</div>
<div class="abs treat" style="top:698px">
  <div class="treat-photo" role="img" aria-label="Photo of a client receiving a hair spa treatment" style="background:radial-gradient(circle at 50% 45%,#9aa6b3,#2b2f36)"></div>
  <div><h4>Hair Spa</h4><p>ipsum dolor sit amet, consectetuer adipiscing elit, sed diam nonummy nibh euismod tincidunt ut laoreet dolore magna aliquam erat volutpat.</p></div>
</div>
<div class="abs treat" style="top:768px">
  <div class="treat-photo" role="img" aria-label="Illustration of a hair colour style" style="background:radial-gradient(circle at 50% 45%,#e6d5d8,#7a2a4a)"></div>
  <div><h4>Hair color</h4><p>Lorem ipsum dolor sit amet, consectetuer adipiscing elit, sed diam nonummy nibh euismod tincidunt ut laoreet dolore magna aliquam erat volutpat.</p></div>
</div>

<footer class="abs footer">
  <div class="abs f-col" style="left:57px;top:28px">
    <h3 class="f-title">Follow Us</h3>
    <div class="social"><span></span><span></span><span></span><span></span></div>
    <h3 class="f-title" style="margin-top:20px">Location</h3>
    <p class="f-text" style="margin-top:8px;line-height:21px">1-22-003-55,<br>Neque porro quisquam,<br>dolor sit amet,<br>your city.</p>
  </div>
  <div class="abs f-col" style="left:263px;top:28px">
    <h3 class="f-title">Information</h3>
    <p class="f-text" style="margin-top:8px">Lorem ipsum dolor sit amet, consectetur adipisicing elit, sed do eiusmod tempor incididunt ut labore et dolore magna aliqua. Ut enim ad minim veniam, quis nostrud exercitation ullamco laboris nisi ut aliquip ex ea commodo consequat.<br><span class="f-link">Read More[...]</span></p>
  </div>
  <div class="abs f-col" style="left:469px;top:28px">
    <h3 class="f-title">Testimonials</h3>
    <p class="f-text" style="margin-top:8px"><span class="quote-mark">&ldquo;</span> Lorem ipsum dolor sit amet, consectetur adipisicing elit, sed do eiusmod tempor incididunt ut labore et dolore magna aliqua. Ut enim ad minim veniam, quis nostrud exercitation ullamco laboris nisi ut aliquip ex ea commodo consequat. <span class="quote-mark">&rdquo;</span></p>
    <p class="cite">- Lorem ipsum dolor</p>
  </div>
  <div class="abs f-col" style="left:675px;top:28px">
    <h3 class="f-title">Contact Us</h3>
    <p class="f-text" style="margin-top:6px;line-height:21px">www.yourcompany(at)salonmail.com<br>Mobile : +12 345 67890<br>Telephone : +00 000 00000<br>Fax : +00 000 00000</p>
  </div>
</footer>

<div class="abs copyright">Company Name © 2014 All Rights Reseverd</div>

</body>
</html>
```